" Pediatra com area de atuaçao em crianças de 0-18 anos em consultório particular. Atendimento classe economica A e B. Coordenadora médica do site crescersaudavel.com.br "

```html
<!DOCTYPE html>
<html lang="pt-BR">
<head>
<meta charset="utf-8">
<title>Papel timbrado – Dra. Helena Moraes</title>
<link rel="stylesheet" href="https://fonts.googleapis.com/css2?family=Open+Sans:wght@400;600&display=swap">
<style>
  :root {
    --backdrop: #6d6d6d;
    --paper: #ffffff;
    --sun: #f6ea1c;
    --lavender: #c3bcdc;
    --teal: #3db3c3;
    --mist: #e4f0f1;
    --ink: #4a4a4a;
    --ink-soft: #555555;
  }
  * { margin: 0; padding: 0; box-sizing: border-box; }
  html, body {
    width: 1200px; height: 1200px; overflow: hidden;
    background: var(--backdrop);
    font-family: "Open Sans", Arial, sans-serif;
  }
  .letterhead {
    position: absolute; left: 233px; top: 103px;
    width: 722px; height: 1015px;
    background: var(--paper);
  }
  .side-stripe { position: absolute; left: 0; width: 26px; }
  .side-stripe--sun { top: 0; height: 545px; background: var(--sun); }
  .side-stripe--lavender { top: 545px; height: 470px; background: var(--lavender); }

  .brand { position: absolute; left: 74px; top: 40px; }
  .brand__dot {
    position: absolute; left: 112px; top: 0;
    width: 30px; height: 30px; border-radius: 50%;
    background: var(--teal);
  }
  .brand__name {
    position: absolute; left: 0; top: 36px; white-space: nowrap;
    font-size: 33px; font-weight: 400; color: var(--ink); letter-spacing: 0.2px;
  }
  .brand__specialty {
    position: absolute; left: 77px; top: 86px; white-space: nowrap;
    font-size: 17px; color: var(--ink-soft); letter-spacing: 5px;
  }

  .patient-fields {
    position: absolute; left: 74px; top: 184px; width: 610px;
    font-size: 18px; color: var(--ink-soft); white-space: nowrap;
  }
  .patient-fields span { position: absolute; top: 0; }
  .field-name { left: 0; }
  .field-height { left: 379px; }
  .field-weight { left: 499px; }

  .motif {
    position: absolute; left: 74px; top: 401px;
    width: 610px; height: 216px; border-radius: 108px;
    background: radial-gradient(ellipse at center, var(--mist) 0%, rgba(228,240,241,0.6) 60%, rgba(255,255,255,0) 100%);
  }

  .footer-band {
    position: absolute; left: 26px; right: 0; bottom: 0; height: 103px;
    background: var(--teal);
  }
  .footer-band__address {
    position: absolute; left: 12px; top: 32px;
    font-size: 11.5px; line-height: 15px; color: #ffffff;
  }
</style>
</head>
<body>
  <main class="letterhead">
    <div class="side-stripe side-stripe--sun"></div>
    <div class="side-stripe side-stripe--lavender"></div>

    <header class="brand">
      <span class="brand__dot"></span>
      <h1 class="brand__name">Dra. Helena Moraes</h1>
      <p class="brand__specialty">Pediatria</p>
    </header>

    <div class="patient-fields">
      <span class="field-name">Nome:__________________________________</span>
      <span class="field-height">Altura: ______</span>
      <span class="field-weight">Peso:______</span>
    </div>

    <div class="motif" role="img" aria-label="Faint decorative motif area in pale aqua"></div>

    <footer class="footer-band">
      <address class="footer-band__address" style="font-style:normal">
        Endereço:Rua das Flores,00 -Bairro Jardim -<br>
        Vale Verde-xx<br>
        Cep:00.000-000
      </address>
    </footer>
  </main>
</body>
</html>
```